Doctors clinic requires stationary designed

We require various types of stationary to be design based on the logo (attached). We require the following:
- Letterhead (A4 Portrait)
- Business Card (must include UV spot on rear)
- With compliments slip (DL Landscape)
- Appointments card (Folded A6)

We are a young clinical practice which boasts a modern and sophisticated approach to medicine so we require something which feels fresh and modern. Please include colours represented in the logo (contrasting teal and grey). We are calling for creative minds to put forth their ideas and we will be actively providing feedback on all designs.

thank you

Clinic

```html
<!DOCTYPE html>
<html lang="en">
<head>
<meta charset="utf-8">
<title>Dr Clara Whitfield – Letterhead</title>
<link rel="stylesheet" href="https://fonts.googleapis.com/css2?family=Open+Sans:wght@400;600&display=swap">
<style>
  :root {
    --backdrop: #dedede;
    --paper: #ffffff;
    --teal: #00806e;
    --sage: #74b086;
    --ink-soft: #6f6f6f;
    --watermark: #f0f0f0;
  }
  * { margin: 0; padding: 0; box-sizing: border-box; }
  html, body {
    width: 1200px; height: 816px; overflow: hidden;
    background: var(--backdrop);
    font-family: "Open Sans", Arial, sans-serif;
  }
  .letterhead {
    position: absolute;
    left: 330px; top: 26px;
    width: 540px; height: 764px;
    background: var(--paper);
    box-shadow: 0 4px 18px rgba(0,0,0,0.12);
  }
  .letterhead__header {
    position: absolute;
    left: 40px; right: 34px; top: 42px;
    display: flex; justify-content: space-between; align-items: flex-start;
  }
  .brand { display: flex; align-items: center; gap: 10px; }
  .brand__mark {
    width: 34px; height: 34px; border-radius: 50%;
    border: 2px solid var(--teal);
  }
  .brand__name {
    font-size: 15px; font-weight: 600; color: var(--teal);
    line-height: 1.1;
  }
  .brand__role {
    font-size: 8.5px; font-weight: 600; color: var(--teal);
    letter-spacing: 0.1px; margin-top: 2px;
  }
  .contact {
    display: flex; gap: 10px;
    font-size: 5.5px; color: var(--ink-soft);
    padding-top: 4px;
  }
  .contact__item { display: flex; align-items: center; gap: 3px; white-space: nowrap; }
  .contact__icon { width: 6px; height: 6px; fill: var(--teal); }
  .watermark {
    position: absolute;
    left: 190px; top: 250px;
    width: 160px; height: 160px; border-radius: 50%;
    border: 3px solid var(--watermark);
  }
  .footer-band {
    position: absolute; left: 0; right: 0; bottom: 44px; height: 7px;
  }
</style>
</head>
<body>
  <main class="letterhead">
    <header class="letterhead__header">
      <div class="brand">
        <div class="brand__mark"></div>
        <div>
          <div class="brand__name">Dr Clara Whitfield</div>
          <div class="brand__role">Obstetrician and Gynaecologist</div>
        </div>
      </div>
      <address class="contact" style="font-style:normal">
        <span class="contact__item">
          <svg class="contact__icon" viewBox="0 0 10 10"><path d="M5 0a3.5 3.5 0 0 0-3.5 3.5C1.5 6 5 10 5 10s3.5-4 3.5-6.5A3.5 3.5 0 0 0 5 0zm0 5a1.4 1.4 0 1 1 0-2.8A1.4 1.4 0 0 1 5 5z"/></svg>
          18 Elmwood Lane, London EC1A 4QT
        </span>
        <span class="contact__item">
          <svg class="contact__icon" viewBox="0 0 10 10"><path d="M2 0.5l2 2-1 1.3c.6 1.3 1.7 2.4 3 3l1.3-1 2 2-1.2 1.7C4.5 9.5.5 5.5.3 1.7z"/></svg>
          020 7946 0321
        </span>
        <span class="contact__item">
          <svg class="contact__icon" viewBox="0 0 10 10"><path d="M0 2h10v6H0z M0 2l5 3.5L10 2" fill="none" stroke="#00806e" stroke-width="1"/></svg>
          info@drwhitfield.com
        </span>
      </address>
    </header>

    <div class="watermark" aria-hidden="true"></div>

    <svg class="footer-band" viewBox="0 0 540 7" preserveAspectRatio="none" aria-hidden="true">
      <polygon points="0,0 380,0 386,7 0,7" fill="var(--teal)"/>
      <polygon points="380,0 540,0 540,7 386,7" fill="var(--sage)"/>
    </svg>
  </main>
</body>
</html>
```